Harborline Talent IT Recruiting firm needs a business card design for Recruiters, Sourcers, and Account

We need business cards that allow us to change all contact info, names, titles (Recruiter, Sourcer, Account Manager, Director, CEO, etc) per person since we have three offices, in three cities, Phoenix, Austin, and Las Vegas. We do recruiting and contractors for IT positions (Developers, Architects, Software Engineers, Security Engineers, Help Desk, DBAs, PMs, Scrum Masters, etc.) Our client companies are very diverse from Crestline 250 to silicone Valley type start-ups.

So, while we what hip, techie, and quirky, it still needs to be professional. Primary color we use is blue, with silver as a secondary color.

Target Market(s)

IT, Technology

Industry/Entity Type

Business

Contact Information for Business Card

Company name: Harborline Talent, Inc.
Website: www.harborlinetalent-example.com
Logos for ProCircle, Quillo, and Roomwall

Name, Title, Office Number, Cell Number, email

Font styles to use
Serif
Sans Serif

Colors
0455a3
d5d5d5

Requirements
Nice to have
• The grey I selected below is not necessary - but, would like silver included. I included a card design (File 3: HTI early trial example.jpg) that I had started on. It's very rough, and not quite what we're looking for, but what we did like is the logo, big, maybe a bit faded, off center, goes out of frame, etc. Still looking for other ideas - you are the pros! But, just an idea of a design element we liked.

```html
<!DOCTYPE html>
<html lang="en">
<head>
<meta charset="utf-8">
<title>Harborline Talent, Inc. – Business Card</title>
<link rel="stylesheet" href="https://fonts.googleapis.com/css2?family=Tenor+Sans&display=swap">
<style>
  :root {
    --ink: #111111;
    --card: #ffffff;
    --mark-tint: #e3eff8;
    --mark-tint-soft: #eef5fb;
    --brand-blue: #0455a3;
    --social-blue: #2f87c9;
  }
  html, body {
    margin: 0;
    padding: 0;
    width: 1200px;
    height: 720px;
    overflow: hidden;
    background: var(--card);
  }
  .card {
    position: relative;
    width: 1200px;
    height: 720px;
    overflow: hidden;
    background: var(--card);
    font-family: "Tenor Sans", "Optima", sans-serif;
    color: var(--ink);
  }
  .brand-mark-backdrop {
    position: absolute;
    left: 270px;
    top: -70px;
    width: 1000px;
    height: 860px;
    border-radius: 50%;
    background: radial-gradient(ellipse at 50% 50%, var(--mark-tint) 0%, var(--mark-tint) 55%, var(--mark-tint-soft) 75%, rgba(238,245,251,0) 100%);
  }
  .text-block {
    position: absolute;
    left: 131px;
    top: 0;
  }
  .line {
    position: absolute;
    left: 0;
    white-space: nowrap;
    margin: 0;
    line-height: 1;
  }
  .company-name { top: 124px; font-size: 55px; }
  .tagline { top: 192px; font-size: 24px; letter-spacing: 3.4px; }
  .person-name { top: 282px; font-size: 42px; }
  .person-title { top: 334px; font-size: 33px; font-style: italic; }
  .contact { font-size: 34px; }
  .contact.office { top: 430px; }
  .contact.cell { top: 479px; }
  .contact.email { top: 527px; }
  .social-row {
    position: absolute;
    left: 0;
    top: 580px;
    display: flex;
    align-items: center;
    gap: 18px;
    white-space: nowrap;
  }
  .network {
    display: flex;
    align-items: center;
    gap: 7px;
    font-size: 22px;
    color: var(--brand-blue);
  }
  .network-square {
    width: 14px;
    height: 14px;
    background: var(--social-blue);
  }
  .handle {
    font-size: 28px;
    color: var(--ink);
    margin-left: 4px;
  }
</style>
</head>
<body>
  <main class="card">
    <div class="brand-mark-backdrop" role="img" aria-label="Large faded brand emblem in pale blue, off-centre and running out of frame"></div>

    <div class="text-block">
      <h1 class="line company-name">Harborline Talent, Inc.</h1>
      <p class="line tagline">RISING TO THE CHALLANGE</p>

      <p class="line person-name">Maren Ellison</p>
      <p class="line person-title">Title</p>

      <p class="line contact office">Office Number</p>
      <p class="line contact cell">Cell Number</p>
      <p class="line contact email">email</p>

      <div class="social-row">
        <span class="network"><span class="network-square"></span>Roomwall</span>
        <span class="network"><span class="network-square"></span>Quillo</span>
        <span class="network"><span class="network-square"></span>ProCircle</span>
        <span class="handle">@marenellisonHT</span>
      </div>
    </div>
  </main>
</body>
</html>
```